Friendbook landing page design

We are a Video Production Company and plan to launch our Business Fan Page soon. We are running a competition and need a design done for the related Friendbook landing page.

The landing page should have the following copy:

Win a Web Video Advertisement Worth $4000!
To enter you must:
1. Vote for the web video advertisement that you enjoy the most (check out the Poll Tab)
2. "Like" our Friendbook Fan Page
3. Explain what an ideal web video advertisement would look like for your business (Post this on our wall)
Conditions apply so check out the Poll tab for more information. Competition ends June 30th so get voting!

I have included some previous marketing material for reference only. You do not need to use this as a style a guide
Updates

Target Market(s)

Business owners or marketing managers

Requirements
Must have
• Lofty Crane-media Logo
web address included: www.loftycm.example
An image needs to accompany the copy
Should not have
• text only

```html
<!DOCTYPE html>
<html lang="en">
<head>
<meta charset="utf-8">
<title>Win a Web Video Advertisement – Lofty Crane-media</title>
<link href="https://fonts.googleapis.com/css2?family=Archivo+Black&family=Arimo:wght@400;700&display=swap" rel="stylesheet">
<style>
  :root{
    --sky:#1aa3e6;
    --sky-dark:#0b6fb6;
    --navy:#0a4e95;
    --row-light:#1d9be0;
    --row-mid:#0f82cc;
    --num-bg:#0a6cb8;
    --orange:#f7941d;
    --orange-light:#fcb040;
    --ink:#2b2b2b;
    --grey-band:#dcdcdc;
    --grey-text:#6a6a6a;
    --white:#ffffff;
    --photo-dark:#1c1c1e;
    --photo-mid:#4a4a4e;
  }
  *{box-sizing:border-box;margin:0;padding:0}
  html,body{width:693px;height:1200px;overflow:hidden;background:var(--white)}
  body{font-family:"Arimo",Arial,sans-serif;position:relative}

  .cta-bar{position:absolute;left:0;top:0;width:693px;height:80px;
    background:linear-gradient(#ffffff,#e6e6e6)}
  .cta-arrow{position:absolute;left:60px;top:2px;width:90px;height:76px}
  .cta-text{position:absolute;left:188px;top:22px;font-weight:700;font-size:27px;color:var(--sky);
    display:flex;align-items:center;gap:12px;letter-spacing:-0.5px;white-space:nowrap}
  .like-chip{display:inline-block;border:1px solid #9aa6bf;background:linear-gradient(#fff,#e9ecf2);
    border-radius:3px;color:#3b4f7a;font-size:16px;font-weight:700;padding:4px 10px;line-height:1}

  .hero{position:absolute;left:0;top:80px;width:693px;height:453px;overflow:hidden}
  .hero-photo{position:absolute;inset:0;
    background:radial-gradient(ellipse at 30% 35%,var(--photo-mid),var(--photo-dark) 70%)}
  .headline{position:absolute;left:0;top:168px;width:693px;transform:rotate(-8deg);
    font-family:"Archivo Black",Arial,sans-serif;text-transform:uppercase;line-height:1;
    color:var(--sky);text-align:center;white-space:nowrap;font-weight:400;
    -webkit-text-stroke:9px var(--white);paint-order:stroke fill}
  .headline span{display:block}
  .headline .l1{font-size:50px;letter-spacing:-1px}
  .headline .l2{font-size:56px;letter-spacing:-1.5px;color:#1283d2}
  .headline .l3{font-size:62px;letter-spacing:-1.5px;color:var(--navy)}
  .headline .price{display:inline;color:var(--orange)}

  .enter-band{position:absolute;left:0;top:533px;width:693px;height:64px;
    background:linear-gradient(var(--orange-light),var(--orange));
    display:flex;align-items:center;justify-content:center;
    font-weight:700;font-size:38px;color:var(--ink);letter-spacing:-0.5px}

  .step{position:absolute;left:0;width:693px;display:flex;align-items:center;
    background:linear-gradient(var(--row-light),var(--row-mid))}
  .step-num{width:117px;height:100%;background:var(--num-bg);display:flex;align-items:center;
    justify-content:center;color:var(--white);font-weight:700;font-size:66px}
  .step-text{flex:1;padding:0 18px 0 22px;color:var(--white);font-weight:700;font-size:22px;line-height:1.35}
  .step-1{top:597px;height:119px}
  .step-1 .step-text{padding-right:30px}
  .step-2{top:720px;height:117px}
  .step-3{top:841px;height:116px}
  .step-3 .step-text{font-size:19.5px}
  .step-like{display:flex;align-items:center;gap:26px;font-size:29px}
  .like-button{display:inline-block;border:2px solid #cfd6e4;background:linear-gradient(#fff,#e4e8f0);
    border-radius:4px;color:#3b4f7a;font-size:24px;font-weight:400;padding:10px 22px;margin-left:12px}

  .terms{position:absolute;left:0;top:960px;width:693px;height:74px;background:var(--grey-band);
    display:flex;align-items:center;justify-content:center;text-align:center;
    color:var(--grey-text);font-weight:700;font-size:18px;line-height:1.3}

  .footer-band{position:absolute;left:0;top:1064px;width:693px;height:96px;
    background:linear-gradient(var(--sky),var(--sky-dark))}
  .brand-box{position:absolute;left:26px;top:1052px;width:196px;height:128px;background:var(--white);
    border:3px solid var(--sky);border-radius:10px;display:flex;flex-direction:column;
    align-items:center;justify-content:center;gap:8px}
  .brand-dot{width:22px;height:22px;border-radius:50%;background:var(--sky)}
  .brand-name{font-weight:700;font-size:19px;color:var(--sky-dark);text-align:center;line-height:1.15}
  .web-button{position:absolute;left:250px;top:1076px;width:418px;height:73px;background:var(--white);
    border-radius:8px;display:flex;align-items:center;justify-content:center;
    font-weight:700;font-size:30px;color:var(--sky-dark)}
</style>
</head>
<body>
  <header class="cta-bar">
    <svg class="cta-arrow" viewBox="0 0 90 76" aria-hidden="true">
      <path d="M20 70 C20 40 40 24 62 22 L62 8 L86 30 L62 52 L62 38 C46 40 34 52 20 70 Z" fill="#1a9ae0" stroke="#0b6fb6" stroke-width="2"/>
    </svg>
    <div class="cta-text">Click on the <span class="like-chip">Like</span> button above</div>
  </header>

  <section class="hero">
    <div class="hero-photo" role="img" aria-label="Photo of a businessman shouting through a large golden megaphone against a dark background"></div>
    <h1 class="headline">
      <span class="l1">Win a web video</span>
      <span class="l2">Advertisement</span>
      <span class="l3">Worth <span class="price">$4000!</span></span>
    </h1>
  </section>

  <div class="enter-band">To Enter You Must</div>

  <div class="step step-1">
    <div class="step-num">1</div>
    <p class="step-text">Vote for the web video advertisement that you enjoy the most (check out the Poll Tab)</p>
  </div>
  <div class="step step-2">
    <div class="step-num">2</div>
    <p class="step-text step-like"><span class="like-button">Like</span>Our Friendbook Fan Page</p>
  </div>
  <div class="step step-3">
    <div class="step-num">3</div>
    <p class="step-text">Explain what an ideal web video advertisement would look like for your business (Post this on our wall)</p>
  </div>

  <div class="terms">Conditions apply so check out the Poll tab for more information.<br>Competition ends June 30th so get voting!</div>

  <footer>
    <div class="footer-band"></div>
    <div class="brand-box">
      <span class="brand-dot"></span>
      <span class="brand-name">Lofty Crane-media</span>
    </div>
    <div class="web-button">www.loftycm.example</div>
  </footer>
</body>
</html>
```